The Kestrel Personal Training Studio Information Card

The front and back of card to give people that walk in to our gym. There are a few things to say on the card. But it also needs to be designed in an attractive way. You can make some of the information bullett points or with icons or graphics. Please look at our website at https://thekestrelfitness-example.com/ . The card will be 4" x 9"

Target Market(s)

High End Clientele who want to train in a private gym

Industry/Entity Type

Fitness

Font styles to use
Serif
Sans Serif
Other font styles liked:
• the same font Vorlex uses on the zuntab

Colors
F0912C
F2A743
F7CA91
FBE8D2
FDF5EE

Requirements
Must have
• A cool look

```html
<!DOCTYPE html>
<html lang="en">
<head>
<meta charset="utf-8">
<title>The Kestrel Personal Training Studio – Information Card</title>
<link href="https://fonts.googleapis.com/css2?family=Open+Sans:ital,wght@0,400;0,600;0,700;0,800;1,700;1,800&family=Roboto:ital,wght@1,900&display=swap" rel="stylesheet">
<style>
:root{
  --board:#7a7a7a;
  --ink:#2b2b2b;
  --charcoal:#333333;
  --night:#2a2a2a;
  --footer:#363636;
  --paper:#ffffff;
  --grey-text:#555555;
  --ember:#f05a1a;
  --ember-deep:#c2360c;
  --ember-glow:#ff8a3d;
  --amber:#f0912c;
  --amber-deep:#c9681a;
  --amber-glow:#f7ca91;
}
*{margin:0;padding:0;box-sizing:border-box}
html,body{width:1200px;height:900px;overflow:hidden}
body{background:var(--board);font-family:"Open Sans",Arial,sans-serif;color:var(--ink);position:relative}

.card{position:absolute;top:133px;width:242px;height:545px;background:var(--paper);overflow:hidden;box-shadow:0 3px 10px rgba(0,0,0,.35)}
.card--ember{--accent:var(--ember);--accent-deep:var(--ember-deep);--accent-glow:var(--ember-glow)}
.card--amber{--accent:var(--amber);--accent-deep:var(--amber-deep);--accent-glow:var(--amber-glow)}
.c1{left:74px}.c2{left:350px}.c3{left:624px}.c4{left:900px}

.board-label{position:absolute;top:706px;width:300px;text-align:center;color:#fff;font-weight:700;font-size:19px;letter-spacing:.5px}
.label-a{left:45px}.label-b{left:595px}

.card-footer{position:absolute;left:0;right:0;bottom:0;height:30px;background:var(--footer);color:#fff;font-size:8.5px;letter-spacing:1.4px;display:flex;align-items:center;justify-content:center}

/* front */
.hero-art{position:absolute;left:0;top:0;width:242px;height:305px;
  background:
    radial-gradient(ellipse 70px 60px at 46px 232px,var(--accent-glow) 0%,transparent 100%),
    radial-gradient(ellipse 120px 90px at 215px 40px,var(--accent) 0%,transparent 100%),
    radial-gradient(ellipse 110px 150px at 175px 165px,rgba(120,70,45,.9) 0%,rgba(70,45,35,.6) 55%,transparent 100%),
    radial-gradient(ellipse 180px 70px at 90px 265px,var(--accent) 0%,transparent 100%),
    linear-gradient(180deg,var(--night) 0%,#353230 45%,var(--accent-deep) 82%,var(--accent) 100%);
  clip-path:polygon(0 0,100% 0,100% 93%,90% 97%,80% 94%,66% 99%,52% 95%,38% 98%,24% 94%,12% 98%,0 95%)}
.headline{position:absolute;left:8px;top:22px;width:110px;text-align:center;color:#fff;font-family:"Roboto",Arial,sans-serif;font-style:italic;font-weight:900;line-height:1}
.headline .big{font-size:22px;display:block}
.headline .accent{font-size:8.6px;color:var(--accent);display:block;margin-top:5px}
.headline .small{font-size:6.8px;display:block;margin-top:3px}
.headline .mid{font-size:17px;display:block;margin-top:5px}

.wordmark{position:absolute;left:0;right:0;top:318px;text-align:center;color:var(--charcoal)}
.wordmark .the{font-size:7px;font-weight:700;display:block;margin-left:-100px}
.wordmark .name{font-size:27px;font-weight:700;line-height:1;display:block;letter-spacing:.5px}
.wordmark .tag{font-size:6.6px;font-weight:600;letter-spacing:1.7px;display:block;margin-top:3px;color:var(--grey-text)}

.start{position:absolute;left:14px;top:384px;width:108px}
.start h2{font-size:10.5px;font-weight:800;font-style:italic;line-height:1.2;color:var(--ink)}
.start h2 span{color:var(--accent)}
.start p{margin-top:5px;font-size:6.1px;line-height:1.38;text-align:justify;color:#333}

.contact-tab{position:absolute;height:15px;background:var(--accent);color:#fff;font-weight:700;font-style:italic;font-size:10px;display:flex;align-items:center;justify-content:center;clip-path:polygon(6% 0,100% 0,100% 100%,0 100%)}
.front-tab{left:132px;top:387px;width:110px}
.contacts{position:absolute;left:138px;top:409px;width:104px;list-style:none}
.contacts li{display:flex;align-items:flex-start;gap:4px;font-size:5.6px;line-height:1.35;margin-bottom:5px;color:#333;white-space:nowrap}
.contacts li.phone{font-size:8px;font-weight:600}
.contacts li.mail{font-size:4.7px;letter-spacing:-.05px}
.contacts svg{flex:none;width:8px;height:8px;margin-top:1px}
.contacts li.mail svg{margin-top:0}

/* back */
.collage-art{position:absolute;left:0;top:0;width:242px;height:238px;
  background:radial-gradient(ellipse at 55% 55%,var(--accent) 0%,var(--accent) 45%,transparent 70%),
             linear-gradient(180deg,#2e2e2e 0%,#3a3a3a 30%,var(--accent) 80%);
  clip-path:polygon(0 0,100% 0,100% 88%,82% 95%,64% 90%,45% 100%,26% 93%,10% 98%,0 92%)}
.back-mark{position:absolute;left:12px;top:22px;color:#fff}
.back-mark .the{font-size:5px;font-weight:700;display:block}
.back-mark .name{font-size:17px;font-weight:700;line-height:1;display:block}
.back-mark .tag{font-size:4.6px;font-weight:600;letter-spacing:1.1px;display:block;margin-top:2px}
.snap{position:absolute;background:linear-gradient(135deg,#d9d4cf,#8c837c);border:2px solid #fff;box-shadow:0 1px 3px rgba(0,0,0,.4)}
.s1{left:16px;top:82px;width:64px;height:66px;transform:rotate(-3deg)}
.s2{left:90px;top:62px;width:68px;height:60px;transform:rotate(-8deg)}
.s3{left:168px;top:40px;width:60px;height:54px;transform:rotate(8deg)}
.s4{left:130px;top:122px;width:84px;height:74px;transform:rotate(3deg);background:linear-gradient(135deg,#cfcfcf,#6f6f6f)}
.s5{left:60px;top:158px;width:62px;height:72px;transform:rotate(-4deg)}

.intro{position:absolute;left:16px;top:245px;width:212px;font-size:5.7px;line-height:1.4;text-align:justify;color:#333}
.intro p+p{margin-top:6px}
.back-tab{left:80px;top:327px;width:90px;clip-path:polygon(8% 0,100% 0,92% 100%,0 100%)}
.sessions-title{position:absolute;left:0;right:0;top:351px;text-align:center;font-size:9.5px;font-weight:600}
.price-table{position:absolute;left:26px;top:368px;width:200px;border:1px solid #555;border-collapse:collapse;font-size:7.4px}
.price-table td{border-bottom:1px solid #555;height:19px;padding:0 5px}
.price-table td.price{width:95px}
.price-table tr.gap td{height:10px}
.price-table tr.partner td{background:var(--accent);color:#fff;text-align:center;height:19px;font-size:7.6px}
.example{position:absolute;left:0;right:0;top:478px;text-align:center;font-size:6.1px;font-weight:600}
.example strong{display:block;margin-top:2px;color:var(--accent);font-size:7.6px;font-weight:700}
</style>
</head>
<body>

<!-- front, ember -->
<section class="card card--ember c1">
  <div class="hero-art" role="img" aria-label="Muscular athlete lifting a dumbbell wrapped in fire, with orange paint-splash smoke"></div>
  <h1 class="headline"><span class="big">A SAFE</span><span class="accent">AND INDIVIDUALIZED</span><span class="small">APPROACH TO STRENGTH</span><span class="mid">TRAINING</span></h1>
  <div class="wordmark"><span class="the">THE</span><span class="name">KESTREL</span><span class="tag">PERSONAL TRAINING STUDIO</span></div>
  <div class="start"><h2><span>HOW DO YOU GET</span><br>STARTED?</h2>
    <p>We schedule prospective clients for a no cost or obligation consultation. At that consultation we will do a movement screen with you. This will allow the trainer to see what level of flexibility and strength you are currently at. You will be able to discuss your goals and other issues (injuries, etc) at that time.</p></div>
  <div class="contact-tab front-tab">CONTACT US</div>
  <ul class="contacts">
    <li class="phone"><svg viewBox="0 0 10 10"><path d="M2 1l2 2-1 1.2c.6 1.2 1.5 2.1 2.8 2.8L7 6l2 2-1.2 1.5C4.5 9.2.8 5.5.5 2.2z" fill="#333"/></svg>(555) 302-7148</li>
    <li><svg viewBox="0 0 10 10"><path d="M5 .5a3.2 3.2 0 00-3.2 3.2C1.8 6.2 5 9.5 5 9.5s3.2-3.3 3.2-5.8A3.2 3.2 0 005 .5z" fill="#333"/><circle cx="5" cy="3.7" r="1.2" fill="#fff"/></svg><span>ASHFORD VALE<br>48 Linden Row,<br>Ashford Vale 00412</span></li>
    <li class="mail"><svg viewBox="0 0 10 10"><circle cx="5" cy="5" r="4.5" fill="#333"/><rect x="2.6" y="3.4" width="4.8" height="3.2" fill="#fff"/></svg>hello@thekestrelfitness-example.com</li>
    <li><svg viewBox="0 0 10 10"><circle cx="5" cy="5" r="4.5" fill="#333"/></svg>thekestrelgym</li>
    <li><svg viewBox="0 0 10 10"><circle cx="5" cy="5" r="4.2" fill="none" stroke="#333"/><path d="M5 2.5V5l1.8 1" stroke="#333" fill="none"/></svg><span>Mon to Fri ( 6 a.m. – 8 pm)<br>Sat (7 a.m–2 pm)</span></li>
  </ul>
  <footer class="card-footer">www.thekestrelfitness-example.com</footer>
</section>

<!-- front, amber -->
<section class="card card--amber c2">
  <div class="hero-art" role="img" aria-label="Muscular athlete lifting a dumbbell wrapped in fire, with orange paint-splash smoke"></div>
  <h1 class="headline"><span class="big">A SAFE</span><span class="accent">AND INDIVIDUALIZED</span><span class="small">APPROACH TO STRENGTH</span><span class="mid">TRAINING</span></h1>
  <div class="wordmark"><span class="the">THE</span><span class="name">KESTREL</span><span class="tag">PERSONAL TRAINING STUDIO</span></div>
  <div class="start"><h2><span>HOW DO YOU GET</span><br>STARTED?</h2>
    <p>We schedule prospective clients for a no cost or obligation consultation. At that consultation we will do a movement screen with you. This will allow the trainer to see what level of flexibility and strength you are currently at. You will be able to discuss your goals and other issues (injuries, etc) at that time.</p></div>
  <div class="contact-tab front-tab">CONTACT US</div>
  <ul class="contacts">
    <li class="phone"><svg viewBox="0 0 10 10"><path d="M2 1l2 2-1 1.2c.6 1.2 1.5 2.1 2.8 2.8L7 6l2 2-1.2 1.5C4.5 9.2.8 5.5.5 2.2z" fill="#333"/></svg>(555) 302-7148</li>
    <li><svg viewBox="0 0 10 10"><path d="M5 .5a3.2 3.2 0 00-3.2 3.2C1.8 6.2 5 9.5 5 9.5s3.2-3.3 3.2-5.8A3.2 3.2 0 005 .5z" fill="#333"/><circle cx="5" cy="3.7" r="1.2" fill="#fff"/></svg><span>ASHFORD VALE<br>48 Linden Row,<br>Ashford Vale 00412</span></li>
    <li class="mail"><svg viewBox="0 0 10 10"><circle cx="5" cy="5" r="4.5" fill="#333"/><rect x="2.6" y="3.4" width="4.8" height="3.2" fill="#fff"/></svg>hello@thekestrelfitness-example.com</li>
    <li><svg viewBox="0 0 10 10"><circle cx="5" cy="5" r="4.5" fill="#333"/></svg>thekestrelgym</li>
    <li><svg viewBox="0 0 10 10"><circle cx="5" cy="5" r="4.2" fill="none" stroke="#333"/><path d="M5 2.5V5l1.8 1" stroke="#333" fill="none"/></svg><span>Mon to Fri ( 6 a.m. – 8 pm)<br>Sat (7 a.m–2 pm)</span></li>
  </ul>
  <footer class="card-footer">www.thekestrelfitness-example.com</footer>
</section>

<!-- back, ember -->
<section class="card card--ember c3">
  <div class="collage-art" role="img" aria-label="Orange paint splash with grid texture behind the photo collage"></div>
  <div class="back-mark"><span class="the">THE</span><span class="name">KESTREL</span><span class="tag">PRIVATE TRAINING STUDIO</span></div>
  <div class="snap s1" role="img" aria-label="Trainer coaching a client with dumbbell curls"></div>
  <div class="snap s2" role="img" aria-label="Client doing a cable exercise against a wooden wall"></div>
  <div class="snap s3" role="img" aria-label="Trainer and client at a rack"></div>
  <div class="snap s4" role="img" aria-label="Black and white photo of a client doing floor exercise"></div>
  <div class="snap s5" role="img" aria-label="Client using suspension straps"></div>
  <div class="intro">
    <p>Our clients have different goals: Build strength, Increase Flexibility, Improve functional and daily movements, Train for an event, or Weight Loss. We will tailor your training program to the specific results you are looking for.</p>
    <p>Some ways of training increase the chance of injury, we do not practice those types of training at The Kestrel. Many of our clients have current or past injuries that can cause problems. We work with them to not aggravate those injuries or allow them to become an obstacle to their workouts.</p>
  </div>
  <div class="contact-tab back-tab">CONTACT US</div>
  <h2 class="sessions-title">ALL SESSIONS ARE 60 MINUTES</h2>
  <table class="price-table">
    <tr><td>1 time per week</td><td class="price">$110 per session</td></tr>
    <tr><td>2 times per week</td><td class="price">$85 per session</td></tr>
    <tr><td>3 times per week</td><td class="price">$80 per session</td></tr>
    <tr class="gap"><td></td><td></td></tr>
    <tr class="partner"><td colspan="2">ADD $40 FOR A PARTNERED SESSION</td></tr>
  </table>
  <p class="example">Example: A Partnered Session (2 people training together) coming<strong>TWICE A WEEK IS $125 PER SESSION</strong></p>
  <footer class="card-footer">www.thekestrelfitness-example.com</footer>
</section>

<!-- back, amber -->
<section class="card card--amber c4">
  <div class="collage-art" role="img" aria-label="Orange paint splash with grid texture behind the photo collage"></div>
  <div class="back-mark"><span class="the">THE</span><span class="name">KESTREL</span><span class="tag">PRIVATE TRAINING STUDIO</span></div>
  <div class="snap s1" role="img" aria-label="Trainer coaching a client with dumbbell curls"></div>
  <div class="snap s2" role="img" aria-label="Client doing a cable exercise against a wooden wall"></div>
  <div class="snap s3" role="img" aria-label="Trainer and client at a rack"></div>
  <div class="snap s4" role="img" aria-label="Black and white photo of a client doing floor exercise"></div>
  <div class="snap s5" role="img" aria-label="Client using suspension straps"></div>
  <div class="intro">
    <p>Our clients have different goals: Build strength, Increase Flexibility, Improve functional and daily movements, Train for an event, or Weight Loss. We will tailor your training program to the specific results you are looking for.</p>
    <p>Some ways of training increase the chance of injury, we do not practice those types of training at The Kestrel. Many of our clients have current or past injuries that can cause problems. We work with them to not aggravate those injuries or allow them to become an obstacle to their workouts.</p>
  </div>
  <div class="contact-tab back-tab">CONTACT US</div>
  <h2 class="sessions-title">ALL SESSIONS ARE 60 MINUTES</h2>
  <table class="price-table">
    <tr><td>1 time per week</td><td class="price">$110 per session</td></tr>
    <tr><td>2 times per week</td><td class="price">$85 per session</td></tr>
    <tr><td>3 times per week</td><td class="price">$80 per session</td></tr>
    <tr class="gap"><td></td><td></td></tr>
    <tr class="partner"><td colspan="2">ADD $40 FOR A PARTNERED SESSION</td></tr>
  </table>
  <p class="example">Example: A Partnered Session (2 people training together) coming<strong>TWICE A WEEK IS $125 PER SESSION</strong></p>
  <footer class="card-footer">www.thekestrelfitness-example.com</footer>
</section>

<div class="board-label label-a">LOGO COLOR</div>
<div class="board-label label-b">LOGO COLOR</div>

</body>
</html>
```